One page website

I'm looking for a landing page for my company. Just a brief description of our medical device technology with some images

Coding

Coded - Design and coding required

```html
<!DOCTYPE html>
<html lang="en">
<head>
<meta charset="utf-8">
<title>Vertaline Medical</title>
<link rel="stylesheet" href="https://fonts.googleapis.com/css2?family=Alfa+Slab+One&family=Montserrat:wght@300;400;500;600;700&display=swap">
<style>
:root{
  --green:#8fd11f;
  --green-dark:#6a9c10;
  --green-text:#86c920;
  --f1:#8fcb2b;--f2:#99d530;--f3:#a4e036;--f4:#b1ec40;
  --contact:#96d820;
  --footer:#a2d63a;
  --ink:#222;
  --muted:#555;
  --blue:#2a9fd8;
  --soft:#f6f6f6;
  --white:#fff;
}
*{box-sizing:border-box;margin:0;padding:0}
html,body{width:733px;height:1200px;overflow:hidden;background:var(--white)}
body{position:relative;font-family:'Montserrat',sans-serif;color:var(--ink)}
.page{position:absolute;left:146px;top:0;width:898px;height:2464px;transform:scale(0.4887);transform-origin:0 0;overflow:hidden}
.abs{position:absolute}
/* header */
.header{left:0;top:0;width:898px;height:60px;background:#f8f8f8}
.brand{left:20px;top:18px;font-weight:700;font-size:18px;color:var(--green)}
.nav{right:36px;top:24px;display:flex;gap:34px;font-size:11px;font-weight:500}
.nav a{color:var(--ink);text-decoration:none}
.nav a.active{color:var(--green)}
/* hero */
.hero{left:0;top:60px;width:898px;height:420px;background:linear-gradient(100deg,#d8d4cf 0%,#b5968a 35%,#9a7364 55%,#c9a88a 80%,#6b5a50 100%)}
.hero::after{content:"";position:absolute;inset:0;background:linear-gradient(180deg,rgba(0,0,0,.05),rgba(0,0,0,.35))}
.hero-copy{left:64px;top:140px;z-index:2;width:590px;color:#fff}
.hero h1{font-family:'Alfa Slab One',serif;font-weight:400;font-size:50px;letter-spacing:3px;line-height:60px;white-space:nowrap}
.hero p{font-weight:300;font-size:23px;line-height:27px;margin-top:4px}
.btn{display:inline-block;background:var(--green);color:#fff;border-radius:16px;font-size:13px;font-weight:600;padding:8px 20px}
.hero .btn{margin-top:26px}
/* features */
.features{left:0;top:480px;width:898px;height:225px;display:flex}
.feature{width:224.5px;text-align:center;color:#fff;padding-top:44px}
.feature svg{height:44px}
.feature h3{font-size:18px;font-weight:700;margin-top:10px}
.feature p{font-size:11px;line-height:13px;margin:14px auto 0;width:130px}
/* mission */
.mission-text{left:0;top:705px;width:450px;height:446px;background:#fff;text-align:center}
.mission-text h2{font-size:34px;letter-spacing:3px;color:var(--green-text);margin-top:58px}
.mission-text p{font-size:20px;line-height:34px;font-weight:500;width:370px;margin:12px auto 0}
.mission-text .btn{margin-top:28px;font-size:13px;padding:13px 34px;border-radius:22px;font-weight:500}
.mission-art{left:450px;top:705px;width:448px;height:446px;background:radial-gradient(circle at 53% 50%,#ffffff 0,#ffffff 27%,#eef5e2 45%,var(--soft) 70%)}
/* problem */
.problem{left:0;top:1151px;width:898px;height:281px;background:linear-gradient(180deg,#74a63a,#5f8d2a 60%,#527d22);text-align:center;color:#fff}
.problem h2{font-size:36px;letter-spacing:3px;font-weight:700;margin-top:42px}
.problem p{font-size:13px;line-height:22.5px;font-weight:500;margin:22px 42px 0}
/* team */
.team{left:0;top:1432px;width:898px;height:413px;background:#f7f7f7;text-align:center}
.team h2{font-size:34px;letter-spacing:3px;color:var(--green-text);margin-top:24px;font-weight:600}
.team .sub{font-size:19px;letter-spacing:1px;font-weight:500;margin-top:4px}
.cards{position:absolute;left:0;top:113px;display:flex;gap:12px}
.card{width:215px;height:280px;background:#fff;border-radius:4px;box-shadow:0 0 6px rgba(0,0,0,.12);padding-top:20px}
.avatar{width:94px;height:94px;border-radius:50%;border:2px solid var(--green);background:linear-gradient(160deg,#c7c2bd,#8b7a70);margin:0 auto}
.card h4{font-size:13px;color:var(--green-text);margin-top:18px;letter-spacing:.5px}
.card .role{font-size:11.5px;color:var(--blue);line-height:17px;letter-spacing:.5px}
.card .bio{font-size:9.5px;line-height:17px;color:var(--muted);margin:12px 12px 0}
/* contact */
.contact{left:0;top:1845px;width:448px;height:323px;background:#fff;text-align:center}
.contact h2{font-size:34px;letter-spacing:3px;color:var(--green-text);margin-top:20px}
.field{display:block;width:372px;height:50px;margin:0 auto;border:1.5px solid var(--green);border-radius:25px;text-align:left;padding:0 30px;line-height:47px;font-size:14px;letter-spacing:2px;color:#aaa}
.f1{margin-top:26px}.f2{margin-top:33px}
.signup{display:block;width:372px;height:50px;margin:33px auto 0;background:var(--green);border-radius:25px;color:#fff;font-size:19px;letter-spacing:3px;line-height:50px;font-weight:500}
.info{left:448px;top:1845px;width:450px;height:323px;background:var(--contact);color:#fff;letter-spacing:2px;font-weight:500}
.info h3{position:absolute;left:115px;top:26px;font-size:18px;font-weight:500}
.info .row{position:absolute;left:48px;display:flex;align-items:center;font-size:19px}
.info .row svg{width:30px;margin-right:36px;flex:none}
/* footer */
.footer{left:0;top:2167px;width:898px;height:251px;background:var(--footer);color:#fff;letter-spacing:2px}
.footer .brand2{position:absolute;left:66px;top:126px;font-size:28px;font-weight:700;letter-spacing:0}
.col{position:absolute;top:52px;font-size:14px;font-weight:500}
.col h5{font-size:16px;font-weight:700;margin-bottom:12px}
.col li{list-style:none;line-height:28px}
.socials{display:flex;gap:18px;margin-top:18px}
.socials span{width:39px;height:39px;border-radius:50%;background:#fff;display:flex;align-items:center;justify-content:center}
.copy{left:0;top:2418px;width:898px;height:46px;background:var(--green-dark);color:#fff;font-size:11px;letter-spacing:1.5px;text-align:center;line-height:46px}
</style>
</head>
<body>
<div class="page">
  <header class="abs header">
    <div class="abs brand">Vertaline</div>
    <nav class="abs nav">
      <a class="active" href="#">HOME</a><a href="#">OUR MISSION</a><a href="#">PROBLEM SOLUTION</a><a href="#">OUR TEAM</a><a href="#">CONTACT US</a>
    </nav>
  </header>

  <section class="abs hero" role="img" aria-label="Photo of a hand resting on a patient's bare shoulder and upper back"></section>
  <div class="abs hero-copy">
    <h1>Vertaline Medical, Inc</h1>
    <p>Vertaline Medical is developing a dynamic non-fusion Vertebral Body tethering system to treat pediatric scoliosis, that allows for additional non-surgical correction over time</p>
    <span class="btn">Read more</span>
  </div>

  <section class="abs features">
    <div class="feature" style="background:var(--f1)">
      <svg viewBox="0 0 44 44"><circle cx="22" cy="24" r="14" fill="#fff"/><text x="22" y="30" font-size="16" text-anchor="middle" fill="#8fcb2b" font-family="Montserrat" font-weight="700">$</text></svg>
      <h3>Cost Savings</h3><p>66% Cost Savings ($50K compared to $150K)</p>
    </div>
    <div class="feature" style="background:var(--f2)">
      <svg viewBox="0 0 44 44"><circle cx="22" cy="22" r="15" fill="none" stroke="#fff" stroke-width="3"/><path d="M22 13v10l7 4" stroke="#fff" stroke-width="3" fill="none"/></svg>
      <h3>Time Savings</h3><p>50% Saving in Surgery Time (1.5-2 hrs compared to 4-6 hrs)</p>
    </div>
    <div class="feature" style="background:var(--f3)">
      <svg viewBox="0 0 44 44"><circle cx="22" cy="22" r="16" fill="#fff"/><path d="M14 22l6 6 11-12" stroke="#a4e036" stroke-width="4" fill="none"/></svg>
      <h3>Self Confidence</h3><p>Confirmed improved self-confidence for surgical recipients</p>
    </div>
    <div class="feature" style="background:var(--f4)">
      <svg viewBox="0 0 44 44"><path d="M6 38V22M6 30h32v8" stroke="#fff" stroke-width="3" fill="none"/><circle cx="24" cy="9" r="6" fill="#fff"/><path d="M24 6v6M21 9h6" stroke="#b1ec40" stroke-width="2"/></svg>
      <h3>Single Treatment</h3><p>There is no need of Extra surgery,only one time single treatment</p>
    </div>
  </section>

  <section class="abs mission-text">
    <h2>Our Mission</h2>
    <p>Develop novel technologies focusing on non-fusion scoliosis correction allowing for non-surgical dynamic adjustment of implants over time.</p>
    <span class="btn">Learn More</span>
  </section>
  <div class="abs mission-art" role="img" aria-label="Illustration of a green medical cross with a heart inside, framed by circular arcs"></div>

  <section class="abs problem" role="img" aria-label="Green-tinted technical render of a spinal screw implant behind the text">
    <h2>Problem We’re Solving</h2>
    <p>Scoliosis affects roughly 5 million children in the US - 150,000 or so are braced, while 40,000 advance to fusion surgery. Bracing starts as early as 3 or 4 years old and continues for years.Fusion surgery is the final option. It is irreversible with a reduction in motion that curtails many activities. A dynamic vertebral body tethering system provides a unique option to avoid fusion surgery, and, potentially, a single treatment event for many long term bracing patients.</p>
  </section>

  <section class="abs team">
    <h2>Our Team Members</h2>
    <p class="sub">Founding Team – Experience in Orthopedic Implants</p>
    <div class="cards">
      <div class="card"><div class="avatar" role="img" aria-label="Portrait of Thomas Reed"></div><h4>Thomas Reed</h4><p class="role">Founder and CEO</p><p class="bio">Co-founder and CEO of SpinaCore Innovations- Acquired by Halvern in 2014 Leadership positions at Marlow Labs and Dentell</p></div>
      <div class="card"><div class="avatar" role="img" aria-label="Portrait of Samir Haddad"></div><h4>Samir Haddad, MD</h4><p class="role">Professor and Chief of Pediatric Orthopedics, WCMC</p><p class="bio" style="margin-top:4px">Professor and Chief of Pediatric Orthopedics, WCMC Previous leadership positions at Flexora, Halvern and Orthiva</p></div>
      <div class="card"><div class="avatar" role="img" aria-label="Portrait of Ravi Menon"></div><h4>Ravi Menon Ph.D</h4><p class="role">Co-Founder Chief<br>Science Officer</p><p class="bio" style="margin-top:4px">Previous Chief Science Officer at SpinaCore Previous leadership positions at Flexora, Halvern and Orthiva</p></div>
      <div class="card"><div class="avatar" role="img" aria-label="Portrait of Arjun Patel"></div><h4>Arjun Patel, MD</h4><p class="role">Doctor</p><p class="bio" style="margin-top:6px">Professor of Surgery and Director of Spine Trauma at Lakeview Medical Center</p></div>
    </div>
  </section>

  <section class="abs contact">
    <h2>Contact Us</h2>
    <span class="field f1">Enter Your Name</span>
    <span class="field f2">Enter Your Email</span>
    <span class="signup">Sign up</span>
  </section>
  <section class="abs info">
    <h3>For More Information</h3>
    <div class="row" style="top:78px"><svg viewBox="0 0 30 22"><rect x="1" y="1" width="28" height="20" fill="#fff"/><path d="M1 1l14 11 14-11" stroke="var(--contact)" stroke-width="2" fill="none"/></svg>info@vertaline.com</div>
    <div class="row" style="top:140px"><svg viewBox="0 0 30 30"><path d="M6 2l6 6-3 4c2 4 5 7 9 9l4-3 6 6-4 5C12 28 2 18 1 6z" fill="#fff"/></svg>(555) 014-2290</div>
    <div class="row" style="top:210px;line-height:21px"><svg viewBox="0 0 30 40"><path d="M15 1a13 13 0 0 1 13 13c0 10-13 25-13 25S2 24 2 14A13 13 0 0 1 15 1z" fill="#fff"/><circle cx="15" cy="14" r="5" fill="var(--contact)"/></svg><span style="text-align:center">220 Harbor Ave Ste B110<br>Portland, OR 97204</span></div>
  </section>

  <footer class="abs footer">
    <div class="brand2">Vertaline</div>
    <div class="col" style="left:213px"><h5>Get Started</h5><ul><li>Home</li><li>Our Mission</li><li>Solution</li><li>Our Team</li><li>Members</li></ul></div>
    <div class="col" style="left:370px"><h5>About Us</h5><ul><li>Company</li><li>Inforormation</li><li>Contact Us</li><li>Reviews</li></ul></div>
    <div class="col" style="left:519px"><h5>Support</h5><ul><li>FAQ</li><li>Features</li><li>Help</li></ul></div>
    <div class="col" style="left:666px"><h5>Social Links</h5>
      <div class="socials">
        <span><svg width="20" height="14" viewBox="0 0 20 14"><rect width="20" height="14" rx="2" fill="var(--footer)"/><path d="M1 1l9 7 9-7" stroke="#fff" stroke-width="1.5" fill="none"/></svg></span>
        <span></span><span></span><span></span>
      </div>
      <h5 style="margin-top:24px;margin-bottom:10px">Our Location</h5>
      <p style="line-height:16px">220 Harbor Ave Ste B110<br>Portland, OR 97204</p>
    </div>
  </footer>
  <div class="abs copy">Copyright © Vertaline Medical LLC @ 2020 | All right reserved</div>
</div>
</body>
</html>
```